Brochure design for HVAC Company

A classic tri-fold brochure design for an air conditioning, refrigeration, and heating company. Would like the designs to be simple (uncluttered), professional, and pull in the logo colors. Attached is the logo and a business card designs. The company name is Bluestem Valley Air Conditioning, Refrigeration, and Heating.

Target Market(s)

Businesses normally food establishments for refrigeration and ice machines. Looking to sell them on maintenance plan: Gold, Silver, and Bronze. The material should help them to understand the services offered: Maintenance, Servicing and Troubleshooting, and Installations of ice machines, commercial refrigeration, and walk-in freezers and air conditioning (duct, ductless, and rooftop)

Industry/Entity Type

Hvac

Font styles to use
Sans Serif

Requirements
Must have
• Include standard information, such as company name, at least two types of contact information (phone, email and post office address), a logo and tagline. It should also include a headline on the front and two or three brief items outlining benefits your organization can provide.
• Tagline is approximately 14 words and 66 characters.
• Looking to inform customers of services offered: maintenance three plans gold, silver, and bronze, servicing and troubleshooting, and installation.
• Products Serviced, maintained, and installed: Commercial refrigeration, Ice Machines, Air Conditioning (both duct, ductless, and rooftop), walk in freezers.
• Call to action is $100 off on signed maintenance contract. $50 off on first service call.
• Use lorem ipsum text to complement the details of the above information. I will add it later before printing.
• Use logo color scheme and any other colors that complement it.
• Would like this to be a word template.
Nice to have
• Can you make this a Microsoft Word template? Sketch is good, or adobe cs4 format.
Should not have
• Photos should NOT be focused on the homeowner. Should BE focused on the commercial side of the business. Photos can be from any of these product areas: commercial refrigeration, ice machine, walk in freezer boxes, and light roof top ac and heating units.

```html
<!DOCTYPE html>
<html lang="en">
<head>
<meta charset="utf-8">
<title>Bluestem Valley – Tri-fold Brochure</title>
<link href="https://fonts.googleapis.com/css2?family=Montserrat:wght@400;600;700;800;900&family=Great+Vibes&display=swap" rel="stylesheet">
<style>
:root{
  --navy:#1d3f8f;
  --navy-deep:#142d6b;
  --orange:#f26b1d;
  --ink:#2b2f3a;
  --grey:#6b6f7a;
  --paper:#ffffff;
  --backdrop:#e9eaec;
}
*{margin:0;padding:0;box-sizing:border-box}
html,body{width:837px;height:1200px;overflow:hidden;background:var(--backdrop);font-family:'Montserrat',sans-serif}
.spread{position:absolute;left:18px;top:340px;width:801px;height:520px;display:flex;box-shadow:0 6px 22px rgba(0,0,0,.18);background:var(--paper)}
.panel{position:relative;width:267px;height:520px;overflow:hidden}
.panel + .panel{border-left:1px solid #e3e5ea}
.pill{position:absolute;left:20px;background:var(--orange);color:#fff;font-size:10px;font-weight:700;padding:5px 14px;border-radius:0 14px 14px 0}
.heading{position:absolute;left:20px;top:44px;font-size:15px;font-weight:800;color:var(--navy)}
.body-copy{position:absolute;left:20px;right:20px;top:68px;font-size:8px;line-height:1.5;color:var(--grey)}
.plans{position:absolute;left:20px;top:190px;display:flex;gap:14px}
.plan{width:44px;height:44px;border-radius:50%;border:3px solid var(--navy-deep)}
.plan.gold{background:radial-gradient(circle,#f5d36b,#c8972a)}
.plan.silver{background:radial-gradient(circle,#f1f2f4,#a7abb3)}
.plan.bronze{background:radial-gradient(circle,#e3a672,#9a5a2c)}
.services{position:absolute;left:20px;right:20px;top:246px;font-size:13px;font-weight:700;color:var(--navy);line-height:1.25}
.web{position:absolute;font-weight:800}
.left-web{left:20px;top:290px;font-size:15px;color:var(--orange)}
.photo{position:absolute}
.photo-ice{left:0;top:320px;width:267px;height:200px;background:linear-gradient(160deg,#b7bcc4,#7b8089 60%,#4e535c)}
.wave{position:absolute;left:0;width:267px}
.offer-top{position:absolute;left:0;right:0;top:16px;text-align:center;font-size:11px;font-weight:700;color:var(--orange);line-height:1.3}
.offer-main{position:absolute;left:0;right:0;top:52px;text-align:center;font-size:18px;font-weight:900;color:var(--navy);line-height:1.2}
.blue-field{position:absolute;left:0;top:112px;width:267px;height:408px;background:linear-gradient(180deg,var(--navy),var(--navy-deep))}
.seal{position:absolute;left:88px;top:132px;width:92px;height:92px;border-radius:50%;background:#fff;border:4px solid #d7dbe4;display:flex;align-items:center;justify-content:center;text-align:center;font-size:10px;font-weight:800;color:var(--navy);line-height:1.2}
.ribbon{position:absolute;left:84px;top:238px;width:100px;height:28px;background:#e9ecf3;color:var(--navy);font-family:'Great Vibes',cursive;font-size:19px;text-align:center;line-height:28px;border-radius:3px}
.name{position:absolute;left:0;right:0;top:282px;text-align:center;color:#fff;font-size:15px;font-weight:800}
.role{position:absolute;left:0;right:0;top:302px;text-align:center;color:#fff;font-size:9px}
.contact{position:absolute;left:92px;top:332px;color:#fff;font-size:8px;line-height:1.7}
.contact-line{display:flex;align-items:center;gap:5px}
.mid-web{left:0;right:0;top:488px;text-align:center;font-size:11px;color:#fff}
.brand{position:absolute;left:0;right:0;top:14px;display:flex;align-items:center;justify-content:center;gap:7px}
.brand-dot{width:18px;height:18px;border-radius:50%;background:var(--orange)}
.brand-name{font-size:15px;font-weight:900;color:var(--navy)}
.brand-sub{position:absolute;left:0;right:0;top:36px;text-align:center;font-size:6px;font-weight:600;color:var(--grey);letter-spacing:.5px}
.photo-room{left:0;top:56px;width:267px;height:290px;background:linear-gradient(180deg,#f1f2f3 0%,#e4ddd3 45%,#b9a996 100%)}
.right-field{position:absolute;left:0;top:340px;width:267px;height:180px;background:var(--navy)}
.title{position:absolute;left:20px;top:378px;font-size:30px;font-weight:900;line-height:1;color:#fff}
.title .accent{color:var(--orange)}
.tagline{position:absolute;left:20px;top:448px;font-size:7px;font-weight:600;color:#fff;letter-spacing:.3px}
.right-web{left:20px;top:490px;font-size:11px;color:#fff}
</style>
</head>
<body>
<main class="spread">

  <section class="panel panel-benefits">
    <div class="pill" style="top:14px">Benefits your organization</div>
    <h2 class="heading">What is Lorem Ipsum?</h2>
    <p class="body-copy">Lorem Ipsum is simply dummy text of the printing and typesetting industry. Lorem Ipsum has been the industry's standard dummy text ever since the 1500s, when an unknown printer took a galley of type and scrambled it to make a type specimen book. It has survived not only five centuries, but also the leap into electronic typesetting.</p>
    <div class="pill" style="top:164px">Customers of services offered</div>
    <div class="plans" aria-label="Gold, Silver and Bronze maintenance plans">
      <div class="plan gold"></div><div class="plan silver"></div><div class="plan bronze"></div>
    </div>
    <p class="services">servicing and troubleshooting, and installation.</p>
    <div class="web left-web">www.bluestemvalleyhvac.com</div>
    <div class="photo photo-ice" role="img" aria-label="Photo of a commercial ice machine being serviced"></div>
    <svg class="wave" style="top:306px" width="267" height="40" viewBox="0 0 267 40" preserveAspectRatio="none">
      <path d="M0 14 C90 40 180 36 267 6 L267 0 L0 0Z" fill="#fff"/>
      <path d="M0 14 C90 40 180 36 267 6" stroke="#f26b1d" stroke-width="4" fill="none"/>
      <path d="M0 22 C90 46 180 42 267 14 L267 20 C180 48 90 52 0 30Z" fill="#1d3f8f"/>
    </svg>
  </section>

  <section class="panel panel-contact">
    <p class="offer-top">$100 OFF ON SIGNED<br>MAINTENANCE CONTRACT</p>
    <p class="offer-main">$50 OFF ON<br>FIRST SERVICE CALL</p>
    <div class="blue-field"></div>
    <svg class="wave" style="top:96px" width="267" height="34" viewBox="0 0 267 34" preserveAspectRatio="none">
      <path d="M0 16 C80 0 180 0 267 20 L267 0 L0 0Z" fill="#fff"/>
      <path d="M0 16 C80 0 180 0 267 20" stroke="#f26b1d" stroke-width="4" fill="none"/>
    </svg>
    <div class="seal">BLUESTEM<br>VALLEY</div>
    <div class="ribbon">Contact us</div>
    <div class="name">DANIEL HARLOW</div>
    <div class="role">Mechanic</div>
    <div class="contact">
      <div class="contact-line">PO Box 218 Millbrook</div>
      <div class="contact-line">NY 12545</div>
      <div class="contact-line"><svg width="8" height="8" viewBox="0 0 10 10"><path d="M2 1l2 2-1 1.5a6 6 0 0 0 2.5 2.5L7 6l2 2-1.5 1.5C4 9 1 6 .5 2.5Z" fill="#fff"/></svg>(555) 014-2277</div>
      <div class="contact-line"><svg width="8" height="8" viewBox="0 0 10 10"><rect x="1" y="2" width="8" height="6" fill="none" stroke="#fff"/><path d="M1 2l4 3 4-3" stroke="#fff" fill="none"/></svg>info@bluestemvalleyhvac.com</div>
    </div>
    <div class="web mid-web">www.bluestemvalleyhvac.com</div>
  </section>

  <section class="panel panel-cover">
    <div class="brand"><span class="brand-dot"></span><span class="brand-name">BLUESTEM VALLEY</span></div>
    <div class="brand-sub">AIR CONDITIONING · REFRIGERATION · HEATING</div>
    <div class="photo photo-room" role="img" aria-label="Photo of a wall-mounted air conditioner in a bright commercial space"></div>
    <div class="right-field"></div>
    <svg class="wave" style="top:318px" width="267" height="40" viewBox="0 0 267 40" preserveAspectRatio="none">
      <path d="M0 30 C90 4 180 4 267 26 L267 40 L0 40Z" fill="#1d3f8f"/>
      <path d="M0 26 C90 0 180 0 267 22" stroke="#f26b1d" stroke-width="5" fill="none"/>
    </svg>
    <h1 class="title">BLUESTEM<br><span class="accent">VALLEY</span></h1>
    <p class="tagline">AIR CONDITIONING, REFRIGERATION AND HEATING</p>
    <div class="web right-web">www.bluestemvalleyhvac.com</div>
  </section>

</main>
</body>
</html>
```